Free Charity Events from KOVAPLAY

The purpose of the landing page is to get all visitors excited about playing in our Free $500 Charity Tournaments. The visitors who click on the landing page will receive 3 free entries into 3 different $500 Charity Tournaments. A $500 Blackjack Tournament, a $500 Texas Holdem Tournament, and a $500 Baccarat Tournament.

We also offer Free Qualifying games 24/7, where players can earn additional entries into our real paying tournaments.

We will reward the winners in each tournament with a share of the $500 and we will reward a worthy cause or charity with $500 as well.

The money comes from advertising shown during the qualifying game.

Our website is currently being developed on our teams development server. Here is a private link to the site. https://dev.kovaplay.net Attached are vector images of our logo.

Also attached are two attempts we made at a landing page.

Target Market(s)

Social Game Players

Industry/Entity Type

Games

Contact Information for Business Card

The purpose of the business card will be to promote our Free Charity Games. There will be a code hand written on the card. (Meaning we will need a white box to write the code in) If the holder of the card enters that code during registration, they will receive 3 free entries into our real cash tournaments. The giver of the card will receive the affiliate bonus for referring a new player.

Font styles to use
Serif
Sans Serif

Colors
9bcb3c
0292cd
ec1f27

Requirements
Must have
• Excitement, i also like humor but that isn't a must, excitement is.
Nice to have
• Humor
Should not have
• Too many words, we are looking for that image that says at least a few hundred words.

```html
<!DOCTYPE html>
<html lang="en">
<head>
<meta charset="utf-8">
<title>KOVAPLAY – Free Charity Tournaments</title>
<link rel="stylesheet" href="https://fonts.googleapis.com/css2?family=Carlito:ital,wght@0,400;0,700;1,700&family=Open+Sans:ital,wght@0,800;1,800&family=Raleway:wght@400;600;700&display=swap">
<style>
:root{
  --blue:#3673b1;
  --green:#7fae47;
  --green-bright:#8cc43c;
  --red:#d8102a;
  --hero-shade:#5c5c5c;
  --ink:#333333;
  --footer-bg:#cccccc;
  --field-line:#cfcfcf;
  --white:#ffffff;
}
*{margin:0;padding:0;box-sizing:border-box}
html,body{width:1023px;height:1200px;overflow:hidden;background:var(--white)}
body{position:relative;font-family:"Raleway",sans-serif;color:var(--ink)}

.hero{position:absolute;left:0;top:0;width:1023px;height:394px;background:var(--hero-shade);overflow:hidden}
.hero-photo{position:absolute;right:0;top:0;width:540px;height:394px;
  background:linear-gradient(100deg,var(--hero-shade) 0%,#6e6a66 25%,#8a7a6c 55%,#9d8f84 80%,#7b746e 100%)}
.brand{position:absolute;left:91px;top:22px;display:flex;align-items:center;gap:12px}
.brand-dot{width:78px;height:78px;border-radius:50%;background:var(--blue)}
.brand-name{font-family:"Carlito",sans-serif;font-weight:700;font-size:76px;color:var(--blue);letter-spacing:1px;line-height:1}
.tagline{position:absolute;left:132px;top:120px;font-family:"Open Sans",sans-serif;font-weight:800;font-size:26px;color:var(--red);letter-spacing:.5px}
.hero-title{position:absolute;left:0;width:600px;text-align:center;font-family:"Open Sans",sans-serif;font-weight:800;line-height:1;
  -webkit-text-stroke:1.5px var(--white);paint-order:stroke fill;text-shadow:2px 2px 2px rgba(0,0,0,.35)}
.play-free{top:175px;left:-2px;font-size:54px;color:var(--blue);letter-spacing:1px}
.three{top:234px;font-size:37px;font-style:italic;color:var(--green-bright)}
.three .amount{color:var(--red)}
.charity{top:278px;font-size:38px;font-style:italic;color:var(--blue)}

.signup{position:absolute;left:0;top:394px;width:1023px;text-align:center}
.signup-title{margin-top:24px;font-family:"Carlito",sans-serif;font-weight:700;font-size:40px;line-height:44px;color:var(--blue);
  text-shadow:2px 2px 3px rgba(0,0,0,.3)}
.games{margin-top:12px;display:flex;justify-content:center;align-items:center;gap:6px;font-family:"Carlito",sans-serif;font-weight:700;font-size:19px;color:var(--green);
  text-shadow:1px 1px 2px rgba(0,0,0,.25)}
.games svg{width:17px;height:17px}

.form{position:absolute;left:292px;top:576px;width:440px}
.row{display:flex;gap:13px}
.field{flex:1;text-align:center}
.field label{display:block;font-size:11px;font-weight:700;letter-spacing:.2px;margin-bottom:3px}
.field input{display:block;width:100%;height:38px;border:1px solid var(--field-line);background:var(--white)}
.row + .row{margin-top:29px}
.divider{margin-top:23px;border:0;border-top:1px solid var(--field-line)}
.submit{display:block;margin:31px 0 0 4px;width:440px;height:36px;border:0;background:var(--green);color:var(--white);
  font-family:"Carlito",sans-serif;font-size:20px;letter-spacing:.3px}

.footer{position:absolute;left:0;top:917px;width:1020px;height:283px;background:var(--footer-bg);text-align:center}
.copyright{margin-top:43px;font-size:11px;color:#555}
.rule{margin:10px auto 0;width:763px;border:0;border-top:1px solid #444}
.rules-title{margin-top:18px;font-size:13px;font-weight:700;color:#444}
.rules-text{margin:41px auto 0;width:770px;font-size:10.5px;line-height:15px;color:#555}
</style>
</head>
<body>
<header class="hero">
  <div class="hero-photo" role="img" aria-label="Photo of an excited young woman cheering while looking at her phone"></div>
  <div class="brand"><span class="brand-dot"></span><span class="brand-name">KOVAPLAY</span></div>
  <p class="tagline">Where Everyone Wins!</p>
  <h1 class="hero-title play-free">PLAY FREE</h1>
  <p class="hero-title three">IN OUR THREE <span class="amount">$500</span></p>
  <p class="hero-title charity">CHARITY TOURNAMENTS</p>
</header>

<main class="signup">
  <h2 class="signup-title">Subscribe email and get 3 free entries<br>into 3 different $500 Charity Tournaments</h2>
  <p class="games">
    <svg viewBox="0 0 24 24"><path d="M12 2l3 6.5 7 .8-5.2 4.8 1.5 7L12 17.6 5.7 21.1l1.5-7L2 9.3l7-.8z" fill="none" stroke="var(--red)" stroke-width="2"/></svg>BLACKJACK
    <svg viewBox="0 0 24 24"><path d="M12 2l3 6.5 7 .8-5.2 4.8 1.5 7L12 17.6 5.7 21.1l1.5-7L2 9.3l7-.8z" fill="none" stroke="var(--red)" stroke-width="2"/></svg>HOLDEM
    <svg viewBox="0 0 24 24"><path d="M12 2l3 6.5 7 .8-5.2 4.8 1.5 7L12 17.6 5.7 21.1l1.5-7L2 9.3l7-.8z" fill="none" stroke="var(--red)" stroke-width="2"/></svg>BACCARAT
  </p>
</main>

<form class="form">
  <div class="row">
    <div class="field"><label for="first">FIRST NAME</label><input id="first" type="text"></div>
    <div class="field"><label for="last">LAST NAME</label><input id="last" type="text"></div>
  </div>
  <div class="row">
    <div class="field"><label for="email">EMAIL</label><input id="email" type="email"></div>
  </div>
  <hr class="divider">
  <button class="submit" type="button">SUBSCRIBE AND GET YOUR THREE FREE ENTRIES</button>
</form>

<footer class="footer">
  <p class="copyright">Copyright 2019 KOVAPLAY, All Rights Reserved.</p>
  <hr class="rule">
  <h3 class="rules-title">OFFICIAL RULES</h3>
  <p class="rules-text">Lorem ipsum dolor sit amet, consectetur adipiscing elit. Mauris velit dolor, rutrum quis neque sit amet, suscipit tempor magna. Vivamus mattis dolor facilisis nisl feugiat mollis. Pellentesque vitae ligula non eros dignissim varius et nec quam. Donec elit ante, blandit vitae placerat a, congue porttitor risus. Sed lobortis tincidunt lectus, id dictum quam aliquet a. Curabitur vulputate enim diam, ac dictum nulla cursus sit amet. Donec quam velit, gravida sit amet gravida non, maximus vel urna. Quisque tempus porta tellus a gravida. Fusce eros leo, volutpat non nisi id, bibendum pretium mauris. Quisque at sem vitae libero sagittis ornare gravida vel elit. Sed sed egestas velit. Suspendisse maximus velit libero, semper viverra massa bibendum non. Ut placerat condimentum velit, non tincidunt velit accumsan vel.</p>
</footer>
</body>
</html>
```